Verlotti Magician

I want the business card for my business to give to people who watch that later I will be employed to show magic here is my website http://www.verlottimagicien.net/I want the interesting design , i am very opened for formal and informal, I watch a lot of design so don't stick to the common shape and form but i hope it can also be produced the thing to write on will be the same as in picture that i will upload , i also will upload the logo for you that so can be easy to useDenis CostilleMagicianMAGICIAN VERLOTTI 17 rue des Tilleuls - 25000 BESANÇON contact@verlottimagicien.net tel. 0384 519 467 tel. 0672 904 153

```html
<!DOCTYPE html>
<html lang="fr">
<head>
<meta charset="utf-8">
<title>Verlotti Magicien – Carte de visite</title>
<link rel="stylesheet" href="https://fonts.googleapis.com/css2?family=Jost:wght@400&family=Montserrat:wght@400;600&display=swap">
<style>
  :root {
    --page: #e4e4e4;
    --card: #efefee;
    --ink: #111111;
    --red: #d42127;
    --grey: #707070;
    --art-dark: #1a1a1a;
    --art-mid: #3a3a3a;
  }
  * { margin: 0; padding: 0; box-sizing: border-box; }
  html, body { width: 1200px; height: 1200px; overflow: hidden; background: var(--page); }
  body { position: relative; font-family: "Montserrat", Arial, sans-serif; }

  .card {
    position: absolute;
    left: 228px;
    width: 744px;
    height: 424px;
    background: var(--card);
  }
  .card--front { top: 136px; }
  .card--back { top: 642px; }

  .brand-name {
    font-family: "Jost", "Futura", sans-serif;
    font-weight: 400;
    color: var(--ink);
    line-height: 1;
    white-space: nowrap;
  }
  .card--front .brand-name {
    position: absolute;
    left: 30px;
    top: 28px;
    font-size: 88px;
    letter-spacing: -1px;
  }

  .portrait {
    position: absolute;
    background: radial-gradient(ellipse at 50% 40%, var(--art-mid), var(--art-dark) 70%);
    border-radius: 48% 48% 14% 14% / 30% 30% 10% 10%;
  }
  .card--front .portrait { left: 484px; top: 34px; width: 228px; height: 284px; }
  .card--back .portrait { left: 290px; top: 85px; width: 166px; height: 208px; }

  .holder-name {
    position: absolute;
    left: 34px;
    top: 216px;
    font-size: 22px;
    font-weight: 600;
    letter-spacing: 0.5px;
    color: var(--red);
  }
  .holder-role {
    position: absolute;
    left: 34px;
    top: 244px;
    font-size: 17px;
    color: var(--grey);
  }

  .contact-list {
    position: absolute;
    left: 34px;
    top: 301px;
    list-style: none;
  }
  .contact-list li {
    display: flex;
    align-items: center;
    height: 24px;
    font-size: 17px;
    color: var(--grey);
  }
  .contact-list svg { width: 18px; height: 18px; margin-right: 9px; flex: none; }

  .studio {
    position: absolute;
    right: 34px;
    top: 351px;
    text-align: right;
    font-size: 17px;
    color: var(--grey);
    line-height: 24px;
  }
  .studio-name { color: var(--red); font-size: 18px; letter-spacing: 0.3px; }

  .card-frame { position: absolute; inset: 0; }
  .card--back .brand-name {
    position: absolute;
    left: 0;
    right: 0;
    top: 292px;
    text-align: center;
    font-size: 42px;
  }
</style>
</head>
<body>

<section class="card card--front" aria-label="Recto de la carte">
  <div class="brand-name">VERLOTTI</div>

  <div class="portrait" role="img" aria-label="Illustration en noir du magicien en veste tenant une carte à jouer"></div>

  <h1 class="holder-name">HUGO MARSENAC</h1>
  <p class="holder-role">Magician</p>

  <ul class="contact-list">
    <li>
      <svg viewBox="0 0 20 20" aria-hidden="true"><circle cx="10" cy="10" r="10" fill="var(--red)"/><path d="M5 8.5c0-2 2.2-3 5-3s5 1 5 3l-1.6.6-.6-1.8c-1.8-.5-3.8-.5-5.6 0l-.6 1.8z M6.5 14l1.2-4h4.6l1.2 4z" fill="#fff"/><circle cx="10" cy="11.8" r="1.2" fill="var(--red)"/></svg>
      0384 519 467
    </li>
    <li>
      <svg viewBox="0 0 20 20" aria-hidden="true"><circle cx="10" cy="10" r="10" fill="var(--ink)"/><rect x="6.5" y="4" width="7" height="12" rx="1.5" fill="#fff"/><rect x="7.8" y="5.5" width="4.4" height="8" fill="var(--ink)"/></svg>
      0672 904 153
    </li>
    <li>
      <svg viewBox="0 0 20 20" aria-hidden="true"><circle cx="10" cy="10" r="10" fill="var(--red)"/><rect x="4.5" y="6" width="11" height="8" fill="#fff"/><path d="M4.5 6l5.5 4.5 5.5-4.5" fill="none" stroke="var(--red)" stroke-width="1.2"/></svg>
      contact@verlottimagicien.net
    </li>
    <li>
      <svg viewBox="0 0 20 20" aria-hidden="true"><circle cx="10" cy="10" r="10" fill="var(--ink)"/><circle cx="10" cy="10" r="6" fill="none" stroke="#fff" stroke-width="1.3"/><path d="M4 10h12M10 4c-3 3-3 9 0 12M10 4c3 3 3 9 0 12" fill="none" stroke="#fff" stroke-width="1.1"/></svg>
      www.verlottimagicien.net
    </li>
  </ul>

  <address class="studio">
    <span class="studio-name">MAGICIAN VERLOTTI</span><br>
    17 rue des Tilleuls - 25000 BESANÇON
  </address>
</section>

<section class="card card--back" aria-label="Verso de la carte">
  <svg class="card-frame" viewBox="0 0 744 424" width="744" height="424" aria-hidden="true">
    <g stroke="var(--ink)" stroke-width="3">
      <line x1="92" y1="60" x2="662" y2="60"/>
      <line x1="52" y1="104" x2="52" y2="330"/>
      <line x1="86" y1="365" x2="646" y2="365"/>
      <line x1="694" y1="90" x2="694" y2="326"/>
    </g>
    <!-- spade -->
    <g transform="translate(56 62)" fill="var(--ink)">
      <path d="M0-26C-6-16-24-8-24 6c0 9 9 14 17 9 2-1 4-3 5-5-1 7-4 12-8 16h20c-4-4-7-9-8-16 1 2 3 4 5 5 8 5 17 0 17-9 0-14-18-22-24-32z"/>
    </g>
    <!-- heart -->
    <g transform="translate(692 57)" fill="var(--red)">
      <path d="M0 26C-8 16-24 6-24-8c0-9 7-14 13-14 5 0 9 3 11 8 2-5 6-8 11-8 6 0 13 5 13 14 0 14-16 24-24 34z"/>
    </g>
    <!-- diamond -->
    <g transform="translate(52 366)" fill="var(--red)">
      <path d="M0-21L20 0 0 21-20 0z"/>
    </g>
    <!-- club -->
    <g transform="translate(686 366)" fill="var(--ink)">
      <circle cx="0" cy="-12" r="11"/>
      <circle cx="-13" cy="6" r="11"/>
      <circle cx="13" cy="6" r="11"/>
      <path d="M-3 0h6c0 10 3 16 8 22h-22c5-6 8-12 8-22z"/>
    </g>
  </svg>

  <div class="portrait" role="img" aria-label="Illustration en noir du magicien en veste tenant une carte à jouer"></div>
  <div class="brand-name">VERLOTTI</div>
</section>

</body>
</html>
```